DL size flyer design for renovations and extensions construction company

We are looking for a flyer design for a construction company specialising in renovations, extensions, and minor building works. The aim is for anyone needing any home construction works to pick up the phone and call us. The flyers will be delivered primarily to letterboxes of homes. We want the flyers to stick out from all the other things people get in the mail by any means possible.

Target Market(s)

The audience we target is residential home owners and are looking to deliver these letters to home letterboxes.

Industry/Entity Type

Residential Construction

Font styles to use
Sans Serif

Colors
000000
ffffff

Requirements
Must have
• 1 - Places for 4 photos with descriptions reading: (1) Bathroom Renovations (4) Kitchen Renovations (3) Home Extensions (4) Outdoor works and landscaping. This may be on the reverse side of the DL flyer.
• 2 - Fonts to be used are (1) Brandon Grotesque (All caps) for main heading, (2) Montserrat SemiBold (All caps) for Headings, (3) Lato for text.
• 3 - Copy of the finished document in PDF and indesign formats.
• 4 - Placeholders for copy (look at the plinvaroq.com website for now)
Nice to have
• A modern looking design.
Should not have
• Not all photos attached are necessarily required. Up to you to use your creativity to decide on the best combination.

```html
<!DOCTYPE html>
<html lang="en">
<head>
<meta charset="utf-8">
<title>Plinvaroq Homes – Renovations Flyer</title>
<link href="https://fonts.googleapis.com/css2?family=Lato:wght@400;700&family=Montserrat:wght@600;800&display=swap" rel="stylesheet">
<style>
  :root {
    --ink: #000000;
    --paper: #ffffff;
    --night: #121214;
    --night-deep: #060607;
    --body-text: #d9d9dc;
    --bar-light: #9a9a9c;
    --bar-mid: #6e6e70;
    --footer-text: #c4c4c8;
  }
  * { margin: 0; padding: 0; box-sizing: border-box; }
  html, body { width: 850px; height: 1200px; overflow: hidden; background: var(--paper); }
  .flyer {
    position: relative;
    width: 850px;
    height: 1200px;
    overflow: hidden;
    background: linear-gradient(180deg, var(--night) 0%, var(--night-deep) 100%);
    font-family: "Lato", Arial, sans-serif;
  }
  .masthead {
    position: absolute;
    left: 0; top: 0;
    width: 850px; height: 126px;
    background: var(--paper);
  }
  .brand {
    position: absolute;
    left: 32px; top: 44px;
    font-family: "Montserrat", Arial, sans-serif;
    font-weight: 800;
    font-size: 46px;
    letter-spacing: 1px;
    color: var(--ink);
    line-height: 1;
  }
  .service-title {
    position: absolute;
    display: flex;
    align-items: center;
    justify-content: center;
    font-family: "Montserrat", Arial, sans-serif;
    font-weight: 600;
    font-size: 22.5px;
    letter-spacing: 0.5px;
    text-transform: uppercase;
    color: #111;
    background: linear-gradient(90deg, rgba(110,110,112,0) 0%, var(--bar-mid) 8%, var(--bar-light) 50%, var(--bar-mid) 92%, rgba(110,110,112,0) 100%);
    white-space: nowrap;
  }
  .service-title--long { font-size: 17.6px; letter-spacing: 0; }
  .service-copy {
    position: absolute;
    font-size: 16.2px;
    line-height: 21px;
    color: var(--body-text);
  }
  .service-copy--justified { text-align: justify; }
  .photo {
    position: absolute;
    border-radius: 0 16px 0 16px;
  }
  .photo--bath { left: 64px; top: 174px; width: 328px; height: 208px;
    background: linear-gradient(135deg, #e8ddd3 0%, #f6f1ec 45%, #c9b8a8 100%); border-radius: 16px 0 16px 0; }
  .photo--kitchen { left: 461px; top: 428px; width: 328px; height: 211px;
    background: linear-gradient(160deg, #f4f4f2 0%, #d6d6d2 55%, #9b9a96 100%); }
  .photo--family { left: 50px; top: 671px; width: 325px; height: 211px;
    background: linear-gradient(170deg, #f2ede6 0%, #d9c7b4 55%, #e9e4dd 100%); border-radius: 16px 0 16px 0; }
  .photo--garden { left: 461px; top: 885px; width: 328px; height: 211px;
    background: linear-gradient(180deg, #3f6a2c 0%, #6f9a3f 45%, #5a3a2a 75%, #cfc8bd 100%); }
  .contact {
    position: absolute;
    left: 0; top: 1152px;
    width: 850px;
    text-align: center;
    font-size: 17px;
    color: var(--footer-text);
  }
</style>
</head>
<body>
<main class="flyer">
  <header class="masthead">
    <div class="brand">PLINVAROQ HOMES</div>
  </header>

  <section class="service service--bathroom">
    <div class="photo photo--bath" role="img" aria-label="Photo of a woman relaxing in a white bathtub with candles"></div>
    <h2 class="service-title" style="left:420px; top:167px; width:390px; height:31px;">Bathroom Renovations</h2>
    <p class="service-copy service-copy--justified" style="left:428px; top:204px; width:388px;">We create custom bathroom renovations of various shapes and sizes to suit a variety of family needs.When considering a bathroom design you will need to take into account a variety of factors including the size of the existing space and whether it can be enlarged, how many people in your family will use the bathroom, if your family size is likely to increase, where the bathroom is located in the home as well as many other considerations.</p>
  </section>

  <section class="service service--kitchen">
    <h2 class="service-title" style="left:43px; top:426px; width:381px; height:32px;">Kitchen Renovations</h2>
    <p class="service-copy" style="left:43px; top:475px; width:392px;">Today's kitchens go further than places to just make a meal - they are the open-plan hub for the modern home.Each kitchen will need to work in with each family's unique needs. That's why it's important to work in with an expert designer and builder on your renovation project.</p>
    <div class="photo photo--kitchen" role="img" aria-label="Photo of a bright modern white kitchen"></div>
  </section>

  <section class="service service--extensions">
    <div class="photo photo--family" role="img" aria-label="Photo of a family lying on a rug in a living room"></div>
    <h2 class="service-title" style="left:432px; top:665px; width:354px; height:33px;">Home Extensions</h2>
    <p class="service-copy service-copy--justified" style="left:428px; top:738px; width:390px;">Today's kitchens go further than places to just make a meal - they are the open-plan hub for the modern home.Each kitchen will need to work in with each family's unique needs. That's why it's important to work in with an expert designer and builder on your renovation project.</p>
  </section>

  <section class="service service--outdoor">
    <h2 class="service-title service-title--long" style="left:40px; top:945px; width:394px; height:32px;">Outdoor Works and Landscaping</h2>
    <p class="service-copy" style="left:43px; top:990px; width:392px;">Today's kitchens go further than places to just make a meal - they are the open-plan hub for the modern home.Each kitchen will need to work in with each family's unique needs. That's why it's important to work in with an expert designer and builder on your renovation project.</p>
    <div class="photo photo--garden" role="img" aria-label="Photo of a landscaped garden with timber planter boxes and lawn"></div>
  </section>

  <footer class="contact">Phone:&nbsp;&nbsp; 0400 555 218, Email:&nbsp;&nbsp; info@plinvaroq.com</footer>
</main>
</body>
</html>
```